Tincture Design for Woman Owned CBD Branf

LumiVelle is a luxery CBD brand for millennial women.

Our premium L Oil contains 500mg of full spectrum CBD derived from specially-sourced hemp for unparalleled purity and quality. Each dropper delivers approximately 20mg of CBD. Available in two flavors, Natural and Mint.

The goal is to design an aesthetically pleasing tincture (bottle dropper) with label and box. The final design should coincide with our brand guidelines and easily marketed for beauty consumers. We are looking for a clean design, the use of raised fonts and/or metallic is fine.

We have 4 other designs we'd like to work on with the winning designer.

Target Market(s)

Millennial Women, Income $75k+

Font styles to use
Other font styles liked:
• See Branding Sheet

Requirements
Must have
• Must follow brand guidelines (see attached for colors, font, etc)
Nice to have
• Raised font or Metallic Print

```html
<!DOCTYPE html>
<html lang="en">
<head>
<meta charset="utf-8">
<title>LumiVelle L Oil Labels</title>
<link href="https://fonts.googleapis.com/css2?family=Montserrat:wght@500&family=Playfair+Display:wght@500;700&display=swap" rel="stylesheet">
<style>
  :root {
    --backdrop: #b1b2b1;
    --paper: #ffffff;
    --pine: #1f6455;
    --honey: #d09b45;
    --leaf-soft: #8fb5a8;
    --leaf-cream: #f6ead6;
  }
  * { margin: 0; padding: 0; box-sizing: border-box; }
  html, body { width: 1200px; height: 1126px; overflow: hidden; }
  body {
    background: var(--backdrop); position: relative;
    font-family: "Playfair Display", serif;
    font-variant-numeric: lining-nums;
  }

  .label {
    position: absolute; left: 65px; width: 1063px; height: 490px;
    background: var(--paper);
  }
  .label--natural { top: 64px; --accent: var(--pine); }
  .label--mint { top: 594px; --accent: var(--honey); }

  .brand-name {
    position: absolute; left: 0; right: 0; text-align: center;
    font-family: "Playfair Display", serif; font-weight: 500;
    color: var(--pine); line-height: 1;
  }
  .label--natural .brand-name { top: 80px; font-size: 52px; letter-spacing: 4px; }
  .label--mint .brand-name { top: 116px; font-size: 36px; letter-spacing: 3px; }

  .brand-dot {
    position: absolute; left: 50%; top: 58px; width: 30px; height: 30px;
    margin-left: -15px; border: 1.5px solid var(--honey); border-radius: 50%;
  }

  .tagline {
    position: absolute; left: 0; right: 0; text-align: center;
    font-family: "Montserrat", sans-serif; font-weight: 500;
    color: var(--honey); text-transform: uppercase; line-height: 1;
  }
  .label--natural .tagline { top: 155px; font-size: 10px; letter-spacing: 5.4px; }
  .label--mint .tagline { top: 166px; font-size: 7.5px; letter-spacing: 4.4px; }

  .rule-thin {
    position: absolute; left: 0; right: 0; top: 201px; height: 11px;
    background: var(--accent);
  }
  .band {
    position: absolute; left: 0; right: 0; top: 218px; height: 225px;
    background: var(--accent);
  }

  .ribbon { position: absolute; left: 440px; top: 0; width: 183px; height: 126px; }

  .product-name {
    position: absolute; left: 440px; width: 183px; top: 12px; text-align: center;
    font-weight: 500; font-size: 48px; line-height: 1;
    color: var(--accent);
  }
  .product-kind {
    position: absolute; left: 440px; width: 183px; top: 76px; text-align: center;
    font-weight: 700; font-size: 28px; letter-spacing: 2px; line-height: 1;
    color: var(--accent);
  }
  .flavour-icon {
    position: absolute; left: 516px; top: 116px; width: 30px; height: 24px;
    border-radius: 50%;
  }
  .label--natural .flavour-icon { background: var(--leaf-soft); }
  .label--mint .flavour-icon { background: var(--leaf-cream); }

  .flavour, .weight {
    position: absolute; left: 0; right: 0; text-align: center;
    color: var(--paper); font-weight: 500; line-height: 1;
  }
  .flavour { top: 144px; font-size: 28px; letter-spacing: 2px; }
  .weight { top: 183px; font-size: 25px; }
</style>
</head>
<body>

  <section class="label label--natural">
    <h1 class="brand-name">LUMIVELLE</h1>
    <p class="tagline">Premium CBD Products</p>
    <div class="rule-thin"></div>
    <div class="band">
      <svg class="ribbon" viewBox="0 0 183 126" aria-hidden="true">
        <polygon points="0,0 183,0 183,126 91.5,110 0,126" fill="#ffffff"/>
        <line x1="11" y1="0" x2="11" y2="118" stroke="#1f6455" stroke-width="1.5"/>
        <line x1="172" y1="0" x2="172" y2="118" stroke="#1f6455" stroke-width="1.5"/>
      </svg>
      <div class="product-name">L Oil</div>
      <div class="product-kind">CBD</div>
      <div class="flavour-icon" role="img" aria-label="Small hemp leaf icon"></div>
      <div class="flavour">Natural</div>
      <div class="weight">20g</div>
    </div>
  </section>

  <section class="label label--mint">
    <span class="brand-dot"></span>
    <h1 class="brand-name">LUMIVELLE</h1>
    <p class="tagline">Premium CBD Products</p>
    <div class="rule-thin"></div>
    <div class="band">
      <svg class="ribbon" viewBox="0 0 183 126" aria-hidden="true">
        <polygon points="0,0 183,0 183,126 91.5,110 0,126" fill="#ffffff"/>
        <line x1="11" y1="0" x2="11" y2="118" stroke="#d09b45" stroke-width="1.5"/>
        <line x1="172" y1="0" x2="172" y2="118" stroke="#d09b45" stroke-width="1.5"/>
      </svg>
      <div class="product-name">L Oil</div>
      <div class="product-kind">CBD</div>
      <div class="flavour-icon" role="img" aria-label="Small mint leaves icon"></div>
      <div class="flavour">Mint</div>
      <div class="weight">20g</div>
    </div>
  </section>

</body>
</html>
```